Simple Business Cards for Self-employed Coach

Simple business card with a design that includes the QLT logo.
Using either only the logo color or additional colors that match the logo.

Meridian Guides reach deeply into the past, gathering wisdom from East and West, while still staying current with the frontiers of new discovery in cognitive science, genetics, and other disciplines. see https://www.brightharborpath.example/what-is-integral-coaching/

Target Market(s)

Coaching Clients in Tokyo /Asia; in business organizations, but also outside

Industry/Entity Type

Life Coaching

Contact Information for Business Card

Lukas Brenning
Certified Meridian Guide

3-2-48 Kamiyoshi
Nakarino 164-0392
Tokyo, Japan

Phone: +81 70 4817 5062
E-Mail: lukas.brenning@mailora.example

Font styles to use
Sans Serif

Colors
00a990

Requirements
Must have
• include uploaded logo
• color fitting with QLT logo color
Nice to have
• simple, elegant design
Should not have
• clutter

```html
<!DOCTYPE html>
<html lang="en">
<head>
<meta charset="utf-8">
<title>Lukas Brenning – Business Card</title>
<link rel="stylesheet" href="https://fonts.googleapis.com/css2?family=Open+Sans:wght@400;600;700&display=swap">
<style>
  :root {
    --teal: #12a990;
    --teal-soft: #9fd3c6;
    --rule: #ececec;
    --paper: #ffffff;
  }
  * { margin: 0; padding: 0; box-sizing: border-box; }
  html, body { width: 1200px; height: 686px; overflow: hidden; background: var(--paper); }
  .card {
    position: relative;
    width: 1200px;
    height: 686px;
    background: var(--paper);
    font-family: "Open Sans", Arial, sans-serif;
    overflow: hidden;
  }
  .side-band { position: absolute; left: 0; top: 0; width: 41px; height: 686px; background: var(--teal); }
  .corner-shape { position: absolute; left: 0; top: 0; }
  .brand-name {
    position: absolute; left: 906px; top: 88px; width: 200px;
    text-align: center; color: var(--paper);
    font-size: 54px; font-weight: 700; letter-spacing: 10px; line-height: 1;
  }
  .icon { position: absolute; }
  .person-name {
    position: absolute; left: 137px; top: 100px;
    font-size: 41px; font-weight: 600; color: var(--teal); line-height: 1.2;
  }
  .person-title {
    position: absolute; left: 137px; top: 148px;
    font-size: 38px; font-weight: 600; color: var(--teal-soft); line-height: 1.2;
  }
  .rule { position: absolute; left: 137px; height: 2px; background: var(--rule); }
  .rule--top { top: 230px; width: 492px; }
  .rule--bottom { top: 442px; width: 795px; }
  .address {
    position: absolute; left: 137px; top: 302px;
    font-size: 24px; font-weight: 600; color: var(--teal-soft); line-height: 33px;
    font-style: normal;
  }
  .address .city { color: var(--teal); font-weight: 700; }
  .contact {
    position: absolute; left: 137px; top: 494px;
    font-size: 34px; color: var(--teal); line-height: 41px;
  }
  .contact-line { display: flex; align-items: center; }
  .contact-mark { width: 46px; display: inline-block; }
</style>
</head>
<body>
<div class="card">
  <div class="side-band"></div>
  <svg class="corner-shape" width="1200" height="686" viewBox="0 0 1200 686" aria-hidden="true">
    <polygon points="736,0 1200,0 1200,201 896,258" fill="var(--teal)"/>
  </svg>
  <div class="brand-name">QLT</div>

  <svg class="icon icon-person" style="left:143px;top:72px" width="28" height="30" viewBox="0 0 28 30" aria-hidden="true">
    <circle cx="14" cy="8" r="7" fill="var(--teal)"/>
    <path d="M1 30 C1 20 7 17 14 17 C21 17 27 20 27 30 Z" fill="var(--teal)"/>
  </svg>
  <div class="person-name">Lukas Brenning</div>
  <div class="person-title">Certified Meridian Guide</div>
  <div class="rule rule--top"></div>

  <svg class="icon icon-pin" style="left:141px;top:262px" width="28" height="36" viewBox="0 0 28 36" aria-hidden="true">
    <path d="M14 1 C6.8 1 1.5 6.5 1.5 13.5 C1.5 22 14 35 14 35 C14 35 26.5 22 26.5 13.5 C26.5 6.5 21.2 1 14 1 Z" fill="var(--teal)"/>
    <circle cx="14" cy="13.5" r="5" fill="var(--paper)"/>
  </svg>
  <address class="address">
    <div>3-2-48 Kamiyoshi</div>
    <div>Nakarino 164-0392</div>
    <div class="city">Tokyo, Japan</div>
  </address>
  <div class="rule rule--bottom"></div>

  <div class="contact">
    <div class="contact-line">
      <span class="contact-mark">
        <svg width="32" height="32" viewBox="0 0 24 24" aria-hidden="true">
          <path d="M6.6 2.5 L9.5 6.5 L7.8 9 C8.8 11.4 12.6 15.2 15 16.2 L17.5 14.5 L21.5 17.4 L19.6 21 C11 21 3 13 3 4.4 Z" fill="none" stroke="var(--teal)" stroke-width="1.6" stroke-linejoin="round"/>
        </svg>
      </span>+81 70 4817 5062
    </div>
    <div class="contact-line"><span class="contact-mark">@</span>lukas.brenning@mailora.example</div>
  </div>
</div>
</body>
</html>
```